Ecommerce site for Curtain Track Company

This is an ecommerce store design and will be based on the xcart ecommerce platform, attached is a design specification and all images to use in the design, you may use any other images you see fit.
This is a new Company so has no logo, if possible please create a logo but if not just use a text based logo in the design this maybe replaced later if required.
We only require a Home page design initially but will also need a category and product page design created, if you can do those also it would be an advantage.
IMPORTANT
We require all designs to be supplied as a full size JPG so we can see the design in detail as the pixel harbor previews are often too small.

```html
<!DOCTYPE html>
<html lang="en">
<head>
<meta charset="utf-8">
<title>Rail Haven – Curtain Tracks</title>
<link href="https://fonts.googleapis.com/css2?family=Arimo:wght@400;700&family=Oswald:wght@500&display=swap" rel="stylesheet">
<style>
:root{
  --page:#ececec;
  --maroon:#4a1f22;
  --maroon-dark:#3b1719;
  --nav:#3a3a3a;
  --nav-active:#050505;
  --cart-bar:#8a8a8a;
  --panel:#ffffff;
  --side-bg:#efefef;
  --side-line:#cfcfcf;
  --text:#444444;
  --text-soft:#555555;
  --title:#4a1f22;
  --white:#ffffff;
}
*{margin:0;padding:0;box-sizing:border-box}
html,body{width:1200px;height:800px;overflow:hidden}
body{background:linear-gradient(#f4f4f4,var(--page));font-family:"Arimo",Arial,sans-serif;color:var(--text);position:relative}
.top-line{position:absolute;left:0;top:0;width:1200px;height:3px;background:var(--nav)}
.brand{position:absolute;left:133px;top:33px;font-weight:700;font-size:34px;letter-spacing:1px;color:var(--nav)}
.account{position:absolute;left:846px;top:0;width:245px;height:35px;background:var(--nav);border-radius:0 0 8px 8px;color:var(--white);font-size:13px;display:flex;align-items:center;padding-left:14px;gap:7px}
.account b{font-weight:700}
.account .sep{width:1px;height:16px;border-left:1px dotted #aaa}
.search{position:absolute;left:846px;top:50px;display:flex}
.search .field{width:181px;height:25px;border:1px solid #c4c4c4;border-right:0;border-radius:5px 0 0 5px;background:var(--white);font-size:12px;color:#888;padding:6px 9px}
.search .go{width:64px;height:25px;background:var(--maroon);border-radius:0 5px 5px 0;color:var(--white);font-size:11px;font-weight:700;display:flex;align-items:center;justify-content:center}
.nav{position:absolute;left:108px;top:91px;width:983px;height:34px;background:linear-gradient(#4a4a4a,var(--nav));border-radius:4px;display:flex;align-items:center}
.nav a{color:var(--white);font-size:13px;font-weight:700;text-decoration:none;padding:0 16px;height:18px;line-height:18px;border-left:1px dotted #888}
.nav a.home{background:var(--nav-active);height:34px;line-height:34px;width:77px;border:0;border-radius:4px 0 0 4px;padding:0 0 0 22px}
.nav a.home+a{border-left:0}
.cartbar{position:absolute;right:0;top:0;width:269px;height:34px;background:linear-gradient(#9a9a9a,#7a7a7a);border-radius:16px 4px 4px 16px;display:flex;align-items:center;padding-left:36px;color:var(--white);font-size:12px;font-weight:700;gap:6px}
.checkout{position:absolute;right:19px;top:6px;width:91px;height:22px;background:var(--maroon);border:1px solid #222;border-radius:5px;font-size:11px;display:flex;align-items:center;justify-content:center;gap:5px}
.panel{position:absolute;left:108px;top:140px;width:983px;height:700px;background:var(--panel);border-radius:8px;box-shadow:0 0 6px rgba(0,0,0,.12)}
.box{position:absolute;left:117px;width:167px;background:linear-gradient(#f7f7f7,#e2e2e2);border:1px solid #cfcfcf;border-radius:5px;overflow:hidden}
.box h3{height:31px;background:var(--maroon);color:var(--white);font-size:12px;font-weight:700;padding:9px 0 0 13px;display:flex;gap:7px}
.box ul{list-style:none}
.box li{height:28px;line-height:28px;padding-left:15px;font-size:12px;color:var(--text-soft);border-bottom:1px dotted var(--side-line)}
.box li:last-child{border-bottom:0}
.box p{font-size:12px;line-height:19px;color:var(--text-soft);padding:6px 15px}
.viewed{padding:16px 0 0 20px}
.viewed .item{margin-bottom:13px}
.viewed .thumb{float:left;width:35px;height:35px;margin:0 4px 0 0;background:linear-gradient(135deg,#6b3a30,#c9a27a,#4a2a22);border:1px solid #999}
.viewed h4{font-size:13px;line-height:16px;color:var(--title);font-weight:700}
.viewed p{padding:4px 18px 0 0;clear:both;line-height:19px}
.cards{display:flex;gap:8px;justify-content:center;padding-top:9px}
.card-shape{width:56px;height:41px;background:var(--white);border:1px solid #555}
.hero{position:absolute;left:296px;top:151px;width:785px;height:214px;border-radius:4px;overflow:hidden;background:linear-gradient(180deg,#c3cfdc 0%,#dde3ea 45%,#b7b8bc 75%,#7c6a62 100%);box-shadow:0 4px 6px rgba(0,0,0,.25)}
.hero .band{position:absolute;left:0;top:107px;width:500px;height:107px;background:rgba(45,45,45,.72);clip-path:polygon(0 0,420px 0,500px 107px,0 107px)}
.hero ul{position:absolute;left:18px;top:120px;list-style:none;font-family:"Oswald",sans-serif;font-size:16px;line-height:22px;color:var(--white);font-weight:500}
.dots{position:absolute;left:1005px;top:383px;display:flex;gap:5px}
.dots i{width:9px;height:9px;background:#777}
.dots i:first-child{background:var(--maroon)}
.about-img{position:absolute;left:312px;top:408px;width:200px;height:182px;background:linear-gradient(135deg,#e8e8e8,#b9b9a4 40%,#d7d7c9 70%,#f1f1f1)}
.about{position:absolute;left:539px;top:405px;width:530px}
.about h2{font-size:18px;color:var(--title);font-weight:700;margin-bottom:6px}
.about p,.about-more{font-size:12px;line-height:21px;color:var(--text-soft)}
.about .lead{font-weight:700;color:#333;line-height:20px}
.about-more{position:absolute;left:311px;top:605px;width:760px}
.crumb{position:absolute;right:140px;top:677px;font-size:12px;color:var(--text-soft)}
.featured{position:absolute;left:296px;top:698px;width:785px;height:46px;background:var(--maroon);border-radius:5px 5px 0 0;color:var(--white);font-size:18px;font-weight:700;padding:12px 0 0 20px}
.featured-area{position:absolute;left:296px;top:744px;width:785px;height:70px;background:#ededed}
.product{position:absolute;top:760px;width:180px;height:60px;background:var(--white);border:1px solid #cfcfcf;border-radius:5px}
.product .pic{margin:14px 0 0 13px;width:152px;height:40px;background:linear-gradient(160deg,#d9d4cc,#9b8f80)}
</style>
</head>
<body>
<div class="top-line"></div>
<div class="brand">RAIL HAVEN</div>
<div class="account"><b>Welcome!</b> Login <span class="sep"></span> Create an account</div>
<div class="search"><div class="field">Type text here</div><div class="go">SEARCH</div></div>

<nav class="nav">
  <a class="home">HOME</a><a>SEARCH</a><a>CUSTOMER SERVICE</a><a>ABOUT US</a><a>FAQ</a><a>CONTACT US</a>
  <div class="cartbar">
    <svg width="18" height="15" viewBox="0 0 18 15"><path d="M1 1h3l2 8h9l2-6H5" fill="none" stroke="#fff" stroke-width="1.6"/><circle cx="7" cy="12.5" r="1.5" fill="#fff"/><circle cx="14" cy="12.5" r="1.5" fill="#fff"/></svg>
    View cart (0)
    <div class="checkout">CHECK OUT <svg width="6" height="9"><path d="M0 0l6 4.5L0 9z" fill="#fff"/></svg></div>
  </div>
</nav>

<div class="panel"></div>

<aside>
  <div class="box" style="top:151px;height:152px">
    <h3>CATEGORIES <svg width="8" height="10"><path d="M1 1l4 4-4 4" fill="none" stroke="#fff" stroke-width="1.5"/></svg></h3>
    <ul><li>Quiet Glide Tracks</li><li>Hand operated Tracks</li><li>Cord operated Tracks</li><li>Automated Tracks</li></ul>
  </div>
  <div class="box" style="top:317px;height:85px">
    <h3>MY CART <svg width="8" height="10"><path d="M1 1l4 4-4 4" fill="none" stroke="#fff" stroke-width="1.5"/></svg></h3>
    <p>You have no items in your shopping cart.</p>
  </div>
  <div class="box" style="top:416px;height:286px">
    <h3>RECENTLY VIEWED <svg width="8" height="10"><path d="M1 1l4 4-4 4" fill="none" stroke="#fff" stroke-width="1.5"/></svg></h3>
    <div class="viewed">
      <div class="item"><div class="thumb" role="img" aria-label="Curtain pole finial thumbnail"></div><h4>Lorem ipsum dolor sit amet</h4><p>Sit amet cons ecte adip is cing aliquam. Curabi tur auctor tellus non.Sit amet cons ecte.</p></div>
      <div class="item"><div class="thumb" role="img" aria-label="Curtain pole finial thumbnail"></div><h4>Lorem ipsum dolor sit amet</h4><p>Sit amet cons ecte adip is cing aliquam. Curabi tur auctor tellus.</p></div>
    </div>
  </div>
  <div class="box" style="top:716px;height:100px">
    <h3>PAYMENT METHOD <svg width="30" height="10"><path d="M23 1l4 4-4 4" fill="none" stroke="#fff" stroke-width="1.5"/></svg></h3>
    <div class="cards"><div class="card-shape"></div><div class="card-shape"></div></div>
  </div>
</aside>

<section class="hero" role="img" aria-label="Bright living room with white sofa, red armchair and tall windows">
  <div class="band"></div>
  <ul>
    <li>✔ FREE UK DELIVERY ON ORDERS OVER £100</li>
    <li>✔ OVER 20 YEARS EXPERIENCE MEASURING / MAKING / FITTING</li>
    <li>✔ 5 YEARS GUARANTEE ON ALL QUIET GLIDE PRODUCTS</li>
    <li>✔ FRIENDLY FAMILY RUN BUSINESS</li>
  </ul>
</section>
<div class="dots"><i></i><i></i><i></i><i></i><i></i></div>

<div class="about-img" role="img" aria-label="Coloured curtain rods with glass finials and orchid flowers"></div>
<div class="about">
  <h2>About Us</h2>
  <p class="lead">Lorem ipsum dolor sit amet, consectetur adipiscing elit. Quisque eu eros nulla.</p>
  <p>Pellentesque at massa nunc, non varius dui. Mauris vitae tellus in eros faucibus rutrum nec vestibulum ligula. Suspendisse potenti. Nulla facilisi. Suspendisse potenti. Suspendisse in ligula sem. Mauris iaculis, elit ac pharetra fringilla, metus lorem vestibulum elit, ut eleifend quam turpis id libero. Aenean sed vestibulum dui. Maecenas nulla nunc, semper sit amet consectetur vitae, lacinia vel libero. Nullam semper diam a nulla vestibulum fermentum. Pellentesque ullamcorper sapien et arcu elementum ac cursus arcu auctor. Mauris iaculis, elit ac pharetra fringilla, metus lorem vestibulum.</p>
</div>
<p class="about-more">Lorem ipsum dolor sit amet, consectetur adipiscing elit. Quisque eu eros nulla. Pellentesque at massa nunc, non varius dui. Mauris vitae tellus in eros faucibus rutrum nec vestibulum ligula. Suspendisse potenti. Nulla facilisi. Suspendisse potenti. Suspendisse in ligula sem. Mauris iaculis, elit ac pharetra fringilla, metus lorem vestibulum elit.</p>
<div class="crumb">Home &gt; Gifts</div>

<h2 class="featured">Featured Products</h2>
<div class="featured-area"></div>
<div class="product" style="left:310px"><div class="pic" role="img" aria-label="Ceiling mounted curtain track"></div></div>
<div class="product" style="left:502px"><div class="pic" role="img" aria-label="Ceiling mounted curtain track"></div></div>
<div class="product" style="left:693px"><div class="pic" role="img" aria-label="Ceiling mounted curtain track"></div></div>
<div class="product" style="left:885px"><div class="pic" role="img" aria-label="Ceiling mounted curtain track"></div></div>
</body>
</html>
```